Property Management Owner Brochure

A bold and professional brochure targeting prospective property owners and investors seeking professional property management services in the Central Texas area. With an in-depth outline of the services we offer, the requirements of each party in the agreement. This brochure will be handed out during marketing events and home owner meetings. Our goal is to increase Brand awareness and increase our door count with quality properties. (photos and verbiage uploaded.)

Target Market(s)

Property Owners and Investors in the rental market

Industry/Entity Type

Property Management

Font styles to use
Serif
Sans Serif
Script

Colors

Designer to choose colors to be used in the design.

Requirements
Must have
• Our Passion, Energy and Experience Get Our Clients the Very Best Results
• Facebook link : @BrookvaleHomesPropertyManagement
• Web Address: www.BrookvaleHomesManagement.example
• Email: Rentals@BrookvaleHomes.example
• Phone #: 254-555-0187
• QLHVA logo, HOMEWARDĀ® / PXR / Equal Housing logo, Brookvale Homes Logo (uploaded)
• We also provide a 24/7/365 Live Phone Service for all incoming phone and email lead requests.
• Our management fees are simple: 10% of monthly rent and a leasing fee of 50% of first full month's rent per lease term. No maintenance up-charges or mark ups.
• Disclaimer: All information deemed reliable but not guaranteed and should be independently verified. Neither listing broker(s) nor Brookvale Homes Management LLC, Brookvale Homes Central Texas LLC and Brookvale Homes Partners LLC, shall be held responsible for typographical errors, misinformation, misprints and shall be held totally harmless.
• Required lawn irrigation, fertilization and maintenance.
Should not have
• Large apartment buildings.

```html
<!DOCTYPE html>
<html lang="en">
<head>
<meta charset="utf-8">
<title>Brookvale Homes – Professional Property Management Brochure</title>
<link rel="stylesheet" href="https://fonts.googleapis.com/css2?family=Raleway:wght@600;700;800;900&family=Open+Sans:wght@400;600;700&family=Nunito:wght@600&display=swap">
<style>
:root{
  --bg:#e8e8e8;
  --paper:#ffffff;
  --ink:#2b2b2b;
  --dark:#262626;
  --gold:#f2c12e;
  --gold-deep:#e0a91a;
  --gold-soft:#f6d35c;
  --muted:#6b6b6b;
  --caption:#4a3b1c;
}
*{box-sizing:border-box;margin:0;padding:0}
html,body{width:739px;height:1200px;overflow:hidden}
body{background:var(--bg);font-family:"Open Sans",sans-serif;color:var(--ink);position:relative}
.page{position:absolute;background:var(--paper);overflow:hidden;box-shadow:0 3px 10px rgba(0,0,0,.18)}
.caption{position:absolute;font-family:"Nunito",sans-serif;font-weight:600;font-size:22px;color:var(--caption)}
svg{display:block}

/* ---------- Front cover ---------- */
.cover{left:389px;top:24px;width:330px;height:466px}
.cover .art{position:absolute;inset:0}
.brand{position:absolute;left:20px;top:30px;display:flex;align-items:center;gap:6px;font-family:"Raleway",sans-serif;font-weight:800;font-size:13px;color:var(--dark);line-height:1.1;width:140px}
.brand-mark{width:12px;height:12px;background:var(--gold);flex:none}
.cover-title{position:absolute;left:20px;bottom:58px;color:#fff;font-family:"Raleway",sans-serif;font-weight:800;font-size:34px;letter-spacing:0;line-height:1;white-space:nowrap}
.cover-sub{position:absolute;left:21px;bottom:36px;color:var(--gold);font-family:"Raleway",sans-serif;font-weight:800;font-size:17px;letter-spacing:.3px;white-space:nowrap}
.cover-url{position:absolute;right:20px;bottom:16px;color:#cfcfcf;font-size:6px}

/* ---------- Back page ---------- */
.back{left:20px;top:24px;width:330px;height:466px;padding:22px 20px}
.tag{display:inline-block;background:var(--gold);color:#fff;font-family:"Raleway",sans-serif;font-weight:800;font-size:8px;padding:3px 10px;border-radius:0 10px 10px 0;letter-spacing:.3px;white-space:nowrap}
.segments{display:flex;justify-content:space-between;margin:12px 4px 10px}
.segment{text-align:center;font-size:5.5px;font-weight:700;color:var(--ink);width:60px}
.segment-dot{width:22px;height:22px;border-radius:50%;background:var(--gold);margin:0 auto 3px}
.intro{font-size:5.6px;line-height:1.55;color:var(--ink);margin-bottom:10px}
.intro::before{content:"\201C";color:var(--gold);font-size:16px;font-weight:700;line-height:0;vertical-align:-6px;margin-right:2px}
.service-box{background:var(--gold-soft);border-radius:10px;padding:10px 12px;margin-bottom:10px}
.service-box li{list-style:none;position:relative;padding-left:9px;font-size:5.4px;line-height:1.55;margin-bottom:3px;color:#3a3220}
.service-box li::before{content:"";position:absolute;left:0;top:2.5px;width:4px;height:4px;border-radius:50%;background:var(--dark)}
.tagline{font-family:"Raleway",sans-serif;font-weight:800;font-size:7px;color:var(--ink);margin-bottom:12px;letter-spacing:.2px}
.connect{display:flex;gap:8px;margin-top:8px}
.contact{list-style:none}
.contact.main{width:176px}
.contact.side{width:106px;padding-top:18px}
.contact li{display:flex;align-items:center;gap:4px;font-size:5.5px;margin-bottom:4px;color:var(--ink);white-space:nowrap}
.contact .hl{color:var(--gold-deep);font-weight:700}
.ico{width:7px;height:7px;border-radius:50%;background:var(--gold);flex:none}
.hatch{position:absolute}

/* ---------- Inner spread ---------- */
.spread{left:20px;top:560px;width:699px;height:494px;background:var(--paper)}
.spread-fold{position:absolute;left:349px;top:0;width:2px;height:100%;background:linear-gradient(90deg,rgba(0,0,0,.12),rgba(0,0,0,0))}
.spread .art{position:absolute;inset:0}
.standards{position:absolute;left:244px;top:26px;color:#fff;font-family:"Raleway",sans-serif;font-weight:800;font-size:15px;letter-spacing:.5px}
.block{position:absolute}
.block .tag{margin-bottom:6px;font-size:7.5px}
.ticks{list-style:none}
.ticks li{position:relative;padding-left:9px;font-size:5.5px;line-height:1.5;margin-bottom:3px}
.ticks li::before{content:"";position:absolute;left:0;top:2.5px;width:4px;height:4px;border-radius:50%;background:var(--gold)}
.spread-url{position:absolute;right:24px;bottom:24px;font-size:6px;color:var(--muted)}
.badges{position:absolute;left:390px;bottom:50px;display:flex;gap:6px;align-items:center}
.badge{width:22px;height:20px;background:var(--dark)}
.badge.wide{width:34px}
.partner{position:absolute;right:40px;bottom:62px;display:flex;align-items:center;gap:5px;font-family:"Raleway",sans-serif;font-weight:800;font-size:12px;color:var(--dark)}
.partner-mark{width:12px;height:12px;border-radius:50%;background:var(--gold)}
</style>
</head>
<body>

<!-- Front cover -->
<section class="page cover">
  <svg class="art" width="330" height="466" viewBox="0 0 330 466">
    <polygon points="0,230 330,120 330,466 0,466" fill="#262626"/>
    <path d="M0,260 C90,200 200,170 330,160 L330,120 C200,130 90,170 0,230Z" fill="#f2c12e"/>
    <polygon points="150,0 330,0 330,118 120,150" fill="#b3b0ad" role="img" aria-label="Photo: property manager meeting with a client at a desk"/>
    <polygon points="40,200 150,150 170,290 60,330" fill="#6d6a66" role="img" aria-label="Photo: hands holding a camera photographing a rental interior"/>
    <polygon points="245,20 255,36 265,20" fill="none" stroke="#262626" stroke-width="2"/>
    <polygon points="275,200 300,188 290,212" fill="none" stroke="#fff" stroke-width="2"/>
    <polygon points="240,250 252,250 246,260" fill="#fff"/>
    <polygon points="130,320 140,306 150,320" fill="#fff"/>
    <g stroke="#fff" stroke-width="1">
      <line x1="200" y1="280" x2="212" y2="300"/><line x1="204" y1="280" x2="216" y2="300"/>
      <line x1="208" y1="280" x2="220" y2="300"/><line x1="212" y1="280" x2="224" y2="300"/>
    </g>
  </svg>
  <div class="brand"><span class="brand-mark"></span>Brookvale Homes Management</div>
  <div class="cover-title">PROFESSIONAL</div>
  <div class="cover-sub">PROPERTY MANAGEMENT</div>
  <div class="cover-url">www.BrookvaleHomesManagement.example</div>
</section>
<div class="caption" style="left:500px;top:496px">Front</div>

<!-- Back page -->
<section class="page back">
  <span class="tag">OFFERING MANAGEMENT SERVICES FOR</span>
  <div class="segments">
    <div class="segment"><div class="segment-dot"></div>SINGLE FAMILY</div>
    <div class="segment"><div class="segment-dot"></div>MULTI - FAMILY</div>
    <div class="segment"><div class="segment-dot"></div>COMMERCIAL</div>
    <div class="segment"><div class="segment-dot"></div>COMMUNITY</div>
  </div>
  <p class="intro">Our philosophy is simple. Our only goal in this business is to have happy clients who are loving ours for life. In a world that has lost its sense of community &amp; the personal "one on one" experience, we stand at the pinnacle &amp; ask you to not settle for average. You deserve the best!</p>
  <ul class="service-box">
    <li>We syndicate to 50+ online rental property websites, getting our rental properties in front of thousands of prospective tenants within 24 hours of the home going on the market.</li>
    <li>Social media plays a prominent role in the lives of prospective tenants. We maintain a consistent posting rate of several posts per week to maintain an active online presence and grow our audience.</li>
    <li>Time and date stamped photos and videos are taken prior to Move-in and at Move-out inspections. Reports with photos are prepared for each Quarterly Inspection.</li>
    <li>Tenants are required to watch a lease overview video, review lease thoroughly and sign the lease in person. By reviewing the lease with Brookvale Homes Management, we are able to answer tenant questions and ensure the tenants have a full understanding of their responsibilities prior to occupying your home.</li>
  </ul>
  <p class="tagline">OUR PASSION, ENERGY AND EXPERIENCE GET OUR CLIENTS THE VERY BEST RESULTS</p>
  <span class="tag">CONNECT WITH US</span>
  <div class="connect">
    <ul class="contact main">
      <li><span class="ico"></span>Austin Metro Area, Fort Hood Area, Temple / Belton</li>
      <li><span class="ico"></span>Rentals@BrookvaleHomes.example</li>
      <li class="hl">Two Convenient Locations to Serve You :</li>
      <li><span class="ico"></span>120 Sample Ridge Drive, Suite 100, Cedar Park, TX 78600</li>
      <li><span class="ico"></span>45 Example Loop, Suite 200, Killeen, TX 76500</li>
      <li><span class="hl">Visit Us On :</span><span class="ico"></span>@BrookvaleHomesPropertyManagement</li>
    </ul>
    <ul class="contact side">
      <li><span class="ico"></span>254-555-0187</li>
      <li><span class="ico"></span>www.BrookvaleHomesManagement.example</li>
      <li><span class="ico"></span>512-555-0144</li>
      <li><span class="ico"></span>254-555-0187</li>
    </ul>
  </div>
  <svg class="hatch" style="right:22px;top:236px" width="26" height="26" viewBox="0 0 26 26">
    <g stroke="#555" stroke-width="1.2"><line x1="0" y1="26" x2="26" y2="0"/><line x1="6" y1="26" x2="26" y2="6"/><line x1="12" y1="26" x2="26" y2="12"/><line x1="18" y1="26" x2="26" y2="18"/></g>
  </svg>
</section>
<div class="caption" style="left:140px;top:496px">Back</div>

<!-- Inner spread -->
<section class="page spread">
  <svg class="art" width="699" height="494" viewBox="0 0 699 494">
    <path d="M120,95 C190,62 260,60 349,62 L349,0 L200,0 C190,40 165,70 120,95Z" fill="#262626"/>
    <polygon points="0,400 140,420 160,494 0,494" fill="#9e9e9b" role="img" aria-label="Photo: hand switching a breaker in an electrical panel"/>
    <path d="M540,200 C600,180 660,170 699,168 L699,360 C640,370 580,380 520,400 C560,340 560,260 540,200Z" fill="#a88a4e" role="img" aria-label="Photo: plumbing pipes under a sink"/>
    <path d="M520,400 C580,380 640,370 699,360 L699,372 C640,382 580,392 520,412Z" fill="#f2c12e"/>
    <path d="M540,200 C600,180 660,170 699,168 L699,156 C660,158 600,168 536,190Z" fill="#f2c12e"/>
    <polygon points="540,225 562,225 551,240" fill="none" stroke="#262626" stroke-width="2"/>
    <polygon points="95,410 118,410 106,428" fill="none" stroke="#262626" stroke-width="2"/>
    <polygon points="420,460 440,460 430,476" fill="none" stroke="#262626" stroke-width="2"/>
    <polygon points="370,320 385,330 372,340" fill="#262626"/>
    <g stroke="#555" stroke-width="1.2"><line x1="250" y1="212" x2="272" y2="190"/><line x1="256" y1="212" x2="272" y2="196"/><line x1="262" y1="212" x2="272" y2="202"/></g>
  </svg>
  <div class="spread-fold"></div>
  <div class="standards">STANDARDS</div>

  <div class="block" style="left:22px;top:110px;width:200px">
    <span class="tag">MARKETING</span>
    <ul class="ticks">
      <li>Sign will be placed in Yard.</li>
      <li>Listing will be input into the Multiple Listing Service and will then syndicate out to numerous marketing sites.</li>
      <li>In office rental listing sheet.</li>
      <li>Extensive Prospective Tenancy Database.</li>
      <li>Weekly Emails to Area Agents.</li>
      <li>Social Media Marketing.</li>
      <li>Licensed agents show our rental properties allowing valuable instant feedback.</li>
      <li>Properties rent quicker.</li>
    </ul>
  </div>
  <div class="block" style="left:22px;top:270px;width:190px">
    <span class="tag">LEASING</span>
    <ul class="ticks">
      <li>Weekly report issued to Owners with updates regarding property interest.</li>
      <li>Extensive applicant tenant checks (i.e. Criminal, Credit, Rental and Background).</li>
      <li>Time and date stamped video prior to commencement of lease and again at tenant move out.</li>
      <li>Tenants come into the office to go over the lease with management prior to keys being released.</li>
      <li>Full-time Leasing Coordinator that is also a seasoned real estate professional.</li>
    </ul>
  </div>
  <div class="block" style="left:228px;top:222px;width:114px">
    <span class="tag" style="font-size:6.5px;padding:3px 8px">REPAIRS &amp; MAINTENANCE</span>
    <ul class="ticks">
      <li>Owners notified on repairs as needed.</li>
      <li>When emergency repairs are required, they are performed and owners are notified.</li>
      <li>Coordinate repairs &amp; maintenance at no charge.</li>
      <li>Required lawn irrigation, fertilization and maintenance.</li>
      <li>Maintenance requests can be made from entry to completion.</li>
      <li>Invoice payments can be made from trust account direct to vendor.</li>
    </ul>
  </div>

  <div class="block" style="left:370px;top:40px;width:120px">
    <span class="tag">FINANCIAL</span>
    <ul class="ticks">
      <li>Fast collection of rental income, continual rent collection with benefits if in breach.</li>
      <li>Direct deposit to owner accounts.</li>
      <li>Monthly account statements available.</li>
      <li>Yearly 1099s sent electronically.</li>
    </ul>
  </div>
  <div class="block" style="left:370px;top:150px;width:160px">
    <span class="tag">GENERAL</span>
    <ul class="ticks">
      <li>We also provide a 24/7/365 Live Phone Service for all incoming phone and email lead requests.</li>
      <li>Online owner and tenant portals let owners and tenants view their accounts, documents, and back-and-forth communication.</li>
      <li>Our management fees are simple: 10% of monthly rent and a leasing fee of 50% of first full month's rent per lease term. No maintenance up-charges or mark ups.</li>
    </ul>
  </div>
  <div class="block" style="left:540px;top:40px;width:140px">
    <span class="tag">INSPECTIONS</span>
    <ul class="ticks">
      <li>Regular routine inspections conducted quarterly and a detailed summary along with photographs uploaded to portal.</li>
      <li>Regular Periodic drive by inspections conducted on properties.</li>
    </ul>
  </div>

  <div class="badges"><span class="badge"></span><span class="badge"></span><span class="badge wide"></span></div>
  <div class="partner"><span class="partner-mark"></span>QLHVA</div>
  <div class="spread-url">www.BrookvaleHomesManagement.example</div>
</section>
<div class="caption" style="left:478px;top:1070px">Inner Side</div>

</body>
</html>
```